Whimsical business cards and stationary for accessories and gifts company
Please use your design expertise!
Whimsical business cards and stationary for accessories and gifts company - Children
Creative Brief
Bright & Fun-filled
Marisa T Palvendo
Designer
Brindlewick, Harlow County
PipandLulaDesigns@brimletmail.com
www.PipAndLulaDesigns.craftvane.com www.friendloop.com/PipandLulaDesigns @PipAndLulaDesigns
Hair Accessories Party Favors Unique Gifts
Concepts
Business Cards for kids golf
Vanta Vanta
Kindly upload the Ai file of your logo.

```html
<!DOCTYPE html>
<html lang="en">
<head>
<meta charset="utf-8">
<title>Pip &amp; Lula – Business Cards</title>
<link rel="stylesheet" href="https://fonts.googleapis.com/css2?family=Questrial&display=swap">
<style>
  :root {
    --plum: #8e1f8f;
    --plum-soft: #b45bb5;
    --ink: #4a4a4a;
    --ink-light: #7a7a7a;
    --card: #ffffff;
    --backdrop: #e9e6e2;
  }
  * { box-sizing: border-box; margin: 0; padding: 0; }
  html, body {
    width: 1200px; height: 904px; overflow: hidden;
    background: var(--backdrop);
    font-family: "Questrial", sans-serif;
  }
  .stage { position: relative; width: 1200px; height: 904px; }
  .card {
    position: absolute; left: 240px;
    width: 720px; height: 411px;
    background: var(--card);
    box-shadow: 0 6px 18px rgba(0,0,0,.18);
    overflow: hidden;
  }
  .card--front { top: 26px; }
  .card--back { top: 467px; }

  /* front */
  .brand-mark {
    position: absolute; left: 50%; top: 100px; transform: translateX(-50%);
    display: flex; flex-direction: column; align-items: center; gap: 12px;
  }
  .brand-mark__dot {
    width: 96px; height: 96px; border-radius: 50%; background: var(--plum);
  }
  .brand-mark__name { color: var(--plum); font-size: 30px; letter-spacing: 1px; white-space: nowrap; }
  .offerings {
    position: absolute; left: 0; right: 0; top: 300px;
    text-align: center; color: var(--plum-soft); font-size: 15px; letter-spacing: .5px;
  }
  .offerings span + span::before { content: "|"; margin: 0 14px; color: var(--plum); }

  /* back */
  .logo {
    position: absolute; left: 42px; top: 120px;
    display: flex; align-items: center; gap: 12px;
  }
  .logo__dot { width: 34px; height: 34px; border-radius: 50%; background: var(--plum); }
  .logo__name { color: var(--plum); font-size: 46px; line-height: 1; white-space: nowrap; }
  .logo__tagline {
    position: absolute; left: 140px; top: 174px;
    color: var(--ink-light); font-size: 9px; letter-spacing: 3px; text-transform: lowercase;
  }
  .person { position: absolute; right: 70px; top: 50px; text-align: right; }
  .person__name { color: var(--plum); font-size: 21px; font-weight: 400; }
  .person__role { color: var(--ink-light); font-size: 12px; margin-top: 4px; }
  .contact {
    position: absolute; left: 42px; top: 246px;
    list-style: none; color: var(--ink); font-size: 14px; line-height: 19px;
  }
  .contact li { display: flex; align-items: center; gap: 8px; white-space: nowrap; }
  .icon { width: 11px; height: 11px; flex: none; }
  .icon--square { background: var(--plum); border-radius: 2px; }
  .decor-mark {
    position: absolute; right: -40px; bottom: -30px;
    width: 230px; height: 230px; border-radius: 50%;
    background: radial-gradient(circle at 40% 40%, var(--plum-soft), var(--plum));
    opacity: .9;
  }
</style>
</head>
<body>
<main class="stage">
  <section class="card card--front" aria-label="Card front">
    <div class="brand-mark">
      <div class="brand-mark__dot" aria-hidden="true"></div>
      <div class="brand-mark__name">pip &amp; lula</div>
    </div>
    <p class="offerings"><span>Hair Accessories</span><span>Party Favors</span><span>Unique Gifts</span></p>
  </section>

  <section class="card card--back" aria-label="Card back">
    <div class="logo">
      <div class="logo__dot" aria-hidden="true"></div>
      <div class="logo__name">pip &amp; lula</div>
    </div>
    <div class="logo__tagline">little couture</div>

    <div class="person">
      <h1 class="person__name">Marisa T Palvendo</h1>
      <p class="person__role">Designer</p>
    </div>

    <ul class="contact">
      <li>Brindlewick, Harlow County</li>
      <li>
        <svg class="icon" viewBox="0 0 12 12" aria-hidden="true"><path d="M3 1l2 2-1 1.5a6 6 0 0 0 3.5 3.5L9 7l2 2-1.5 1.5C6 10.5 1.5 6 1.5 2.5z" fill="var(--plum)"/></svg>
        (555) 014-2287
      </li>
      <li>
        <svg class="icon" viewBox="0 0 12 12" aria-hidden="true"><rect x="1" y="2.5" width="10" height="7" rx="1" fill="none" stroke="var(--plum)" stroke-width="1.3"/><path d="M1.5 3l4.5 3.5L10.5 3" fill="none" stroke="var(--plum)" stroke-width="1.2"/></svg>
        PipandLulaDesigns@brimletmail.com
      </li>
      <li><span class="icon icon--square" aria-hidden="true"></span>www.PipAndLulaDesigns.craftvane.com</li>
      <li><span class="icon icon--square" aria-hidden="true"></span>www.friendloop.com/PipandLulaDesigns</li>
      <li><span class="icon icon--square" aria-hidden="true"></span>@PipAndLulaDesigns</li>
    </ul>

    <div class="decor-mark" aria-hidden="true"></div>
  </section>
</main>
</body>
</html>
```